Global social media analytics company needs business card design

We need an updated business card design to align with our new website - plumvantix.com -

I would also like a favicon designed as well.

Target Market(s)

CEOs, CMOs go big companies

Industry/Entity Type

Business

Contact Information for Business Card

Room for the following:
Address
Main telephone
Direct telephone or cell phone
twitter handle

Colors
aaaaaa

Requirements
Must have
• Attention to detail; style.
• Use the logo color from our website - which is gray

```html
<!DOCTYPE html>
<html lang="en">
<head>
<meta charset="utf-8">
<title>Plumvantix Stationery</title>
<link rel="stylesheet" href="https://fonts.googleapis.com/css2?family=Questrial&display=swap">
<style>
  :root{
    --stage:#1f1f1f;
    --paper:#ffffff;
    --brand:#aaaaaa;
    --brand-dark:#8f8f8f;
    --surface-grey:#a3a3a3;
    --surface-grey-deep:#8a8a8a;
    --ink:#5a5a5a;
    --ink-soft:#8a8a8a;
    --faint:#efefef;
    --signature:#3a4fa8;
  }
  *{box-sizing:border-box;margin:0;padding:0}
  html,body{width:1200px;height:1200px;overflow:hidden}
  body{background:var(--stage);font-family:"Questrial",sans-serif;color:var(--ink);position:relative}

  .piece{position:absolute;overflow:hidden;background:var(--paper)}
  .brand{display:flex;align-items:center;gap:5px;position:absolute}
  .brand-dot{border-radius:50%;background:var(--brand);flex:none}
  .brand-name{color:var(--brand);font-weight:400;letter-spacing:-0.2px;line-height:1}
  .brand.on-grey .brand-dot{background:#fff}
  .brand.on-grey .brand-name{color:#fff}
  .deco-circle{position:absolute;border-radius:50%}

  /* Letterhead */
  .letterhead{left:149px;top:60px;width:430px;height:595px}
  .letterhead .brand{left:38px;top:32px}
  .letterhead .brand-dot{width:30px;height:30px}
  .letterhead .brand-name{font-size:15px}
  .letter{position:absolute;left:38px;top:122px;width:348px;font-size:6px;line-height:1.45}
  .letter p{margin-bottom:7px}
  .letter .recipient{margin:6px 0 22px}
  .letter .salutation{font-weight:700;margin-bottom:10px;font-size:6.5px}
  .signature{display:block;width:54px;height:28px;background:linear-gradient(90deg,rgba(58,79,168,.25),rgba(58,79,168,.12));border-radius:3px;position:absolute;left:60px;top:-4px}
  .signoff{position:relative}
  .letterhead .deco-circle{width:210px;height:210px;right:-50px;bottom:-70px;background:var(--faint)}
  .letter-footer{position:absolute;left:38px;bottom:26px;font-size:5.5px;line-height:1.5;color:var(--ink-soft)}

  /* Folder */
  .folder{left:620px;top:62px;width:419px;height:593px;border-radius:4px;
    background:linear-gradient(180deg,var(--surface-grey) 0%,var(--surface-grey-deep) 100%)}
  .folder-spine{position:absolute;left:18px;top:0;bottom:0;width:1px;background:rgba(255,255,255,.35)}
  .folder-spine.second{left:26px}
  .folder .brand{right:36px;top:54px}
  .folder .brand-dot{width:44px;height:44px}
  .folder .brand-name{font-size:19px}
  .folder .deco-circle{width:290px;height:290px;right:-40px;bottom:-60px;background:rgba(255,255,255,.08)}

  /* Envelope front */
  .envelope-front{left:149px;top:707px;width:430px;height:198px}
  .envelope-front .brand{left:22px;top:20px}
  .envelope-front .brand-dot{width:28px;height:28px}
  .envelope-front .brand-name{font-size:12px}
  .sender{position:absolute;left:55px;top:48px;font-size:5px;line-height:1.5;color:var(--ink-soft)}

  /* Envelope back */
  .envelope-back{left:622px;top:707px;width:418px;height:198px}
  .envelope-back .flap{position:absolute;left:0;top:0}
  .flap-mark{position:absolute;left:196px;top:18px;width:26px;height:26px;border-radius:50%;background:#fff}

  /* Compliment slip */
  .compliment-slip{left:622px;top:952px;width:401px;height:186px}
  .compliment-slip .brand{left:22px;top:24px}
  .compliment-slip .brand-dot{width:30px;height:30px}
  .compliment-slip .brand-name{font-size:13px}
  .compliment-slip .deco-circle{width:130px;height:130px;right:-20px;bottom:-50px;background:var(--faint)}
  .slip-title{position:absolute;left:22px;bottom:26px;font-size:7px;letter-spacing:.3px;color:var(--ink)}
  .slip-footer{position:absolute;left:22px;bottom:10px;font-size:5px;line-height:1.5;color:var(--ink-soft)}

  /* Business cards */
  .card-front{left:181px;top:1039px;width:198px;height:98px}
  .card-front .brand{left:14px;top:20px}
  .card-front .brand-dot{width:16px;height:16px}
  .card-front .brand-name{font-size:8px}
  .card-divider{position:absolute;left:108px;top:14px;bottom:14px;width:1px;background:#e3e3e3}
  .card-address{position:absolute;left:26px;top:58px;font-size:4px;line-height:1.5;color:var(--ink-soft)}
  .card-person{position:absolute;left:114px;top:32px;font-size:4px;line-height:1.5;color:var(--ink-soft)}
  .card-person .name{font-size:5.5px;color:var(--ink);letter-spacing:.3px}
  .card-person .role{margin-bottom:5px}
  .card-back{left:390px;top:1039px;width:198px;height:98px;
    background:linear-gradient(180deg,var(--surface-grey),var(--surface-grey-deep))}
  .card-back .brand{left:14px;top:40px}
  .card-back .brand-dot{width:16px;height:16px}
  .card-back .brand-name{font-size:8px}
  .card-back .deco-circle{width:100px;height:100px;right:-20px;top:10px;background:rgba(255,255,255,.1)}
</style>
</head>
<body>

  <section class="piece letterhead">
    <div class="brand"><span class="brand-dot"></span><span class="brand-name">plumvantix</span></div>
    <div class="letter">
      <div class="date">30.02.2015</div>
      <div class="recipient">Recipient's name<br>Kastanienweg 7<br>10437 Berlin<br>Germany</div>
      <div class="salutation">Dear sir,</div>
      <p>Communication sits at the heart of every relationship we build. Our team studies how people talk, share and respond across every social channel, then turns those signals into clear direction for leaders who need answers quickly.</p>
      <p>Letters still carry a weight that quick messages rarely match. A printed page shows care, sets a tone and stays on the desk long after a screen has been closed. We believe that attention to detail belongs in every form of contact.</p>
      <p>Please find enclosed a short summary of our services together with recent results from our global panel. We would be glad to arrange a meeting at a time that suits you.</p>
      <div class="signoff">Yours Sincerely,<br><strong>Lena Morrow</strong>
        <span class="signature" role="img" aria-label="Handwritten signature of Lena Morrow"></span>
      </div>
    </div>
    <span class="deco-circle"></span>
    <div class="letter-footer">2210 Harborline Ave. 3rd Fl. Westbrook, ME 04092, USA<br>T: +1 207 555 0142 · E: info@plumvantix.com · www.plumvantix.com</div>
  </section>

  <section class="piece folder">
    <span class="folder-spine"></span><span class="folder-spine second"></span>
    <div class="brand on-grey"><span class="brand-dot"></span><span class="brand-name">plumvantix</span></div>
    <span class="deco-circle"></span>
  </section>

  <section class="piece envelope-front">
    <div class="brand"><span class="brand-dot"></span><span class="brand-name">plumvantix</span></div>
    <div class="sender">2210 Harborline Ave. 3rd Fl.<br>Westbrook, ME 04092, USA</div>
  </section>

  <section class="piece envelope-back">
    <svg class="flap" width="418" height="62" viewBox="0 0 418 62" aria-hidden="true">
      <polygon points="0,0 418,0 406,50 12,50" fill="var(--surface-grey)"/>
      <polygon points="12,50 406,50 398,58 20,58" fill="#d6d6d6"/>
    </svg>
    <span class="flap-mark"></span>
  </section>

  <section class="piece card-front">
    <div class="brand"><span class="brand-dot"></span><span class="brand-name">plumvantix</span></div>
    <div class="card-address">2210 Harborline Ave. 3rd Fl.<br>Westbrook, ME 04092, USA</div>
    <span class="card-divider"></span>
    <div class="card-person">
      <div class="name">DANA WHITLOCK</div>
      <div class="role">Marketing Manager</div>
      T: +1 207 555 0142<br>E: info@plumvantix.com<br>W: www.plumvantix.com
    </div>
  </section>

  <section class="piece card-back">
    <span class="deco-circle"></span>
    <div class="brand on-grey"><span class="brand-dot"></span><span class="brand-name">plumvantix</span></div>
  </section>

  <section class="piece compliment-slip">
    <div class="brand"><span class="brand-dot"></span><span class="brand-name">plumvantix</span></div>
    <span class="deco-circle"></span>
    <div class="slip-title">WITH COMPLIMENTS</div>
    <div class="slip-footer">2210 Harborline Ave. 3rd Fl. Westbrook, ME 04092, USA<br>T: +1 207 555 0142 · E: info@plumvantix.com · www.plumvantix.com</div>
  </section>

</body>
</html>
```